New Business Card Design Project

We need to enhance the look and feel of our brand. We are starting with the business card and will hopefully expand to letter head, website, etc. The firm is based in Kolding Denmark and invests with global pension funds and for mutual fund investors alike. We would like to see an innovative use of the companies logo (star on the website - www.tidemarkharbor.com) and a broader use of a color palette. Presently it is dominantly shades of blue. The firm wants to convey a sense they are a creative investment team that understands all the risks in the emerging markets and have the skills to perform in an environment of uncertainty.

Presently, we have three locations: Kolding Denmark, Glendale CA USA, Zurich Switzerland. We also have a prominently displayed bar code square on a solid dark blue back that will take smart phone users to the firm's website. I am indifferent to its inclusion., Details for my new Business Card Design Project will be added soon.
Updates

Reason: Designers, I am working with on getting feedback from both US and Danish partners on preferences. That is taking slightly more time than expected. Thanks for you patience. Nice work. PLM

Target Market(s)

The target market is a combination of institutional and retail investors. The european arm uses a card similar to a couple of those submitted.

Industry/Entity Type

Environment

Requirements
Must have
• The company's Star Logo. See www.tidemarkharbor.com. It may be used in its current form or some new clever way. The founders are Danish and have a strong affinity for it.
Nice to have
• The new materials may be solely used in the north America and distributed in Australia as well. Therefore, we may try something new in these markets. I'd prefer to see a broader use of the color spectrum, not simply blue.
Should not have
• The card should not look and feel like a bank, insurance company, or a traditional money manager.

```html
<!DOCTYPE html>
<html lang="en">
<head>
<meta charset="utf-8">
<title>Tidemark Harbor – Business Card</title>
<link rel="stylesheet" href="https://fonts.googleapis.com/css2?family=PT+Sans:wght@400;700&display=swap">
<style>
  :root {
    --page-bg: #ffffff;
    --card-dark: #10152e;
    --card-light: #ffffff;
    --brand-sky: #5bb8e6;
    --brand-navy: #1d3a6b;
    --text-main: #1a1a1a;
    --text-soft: #b7a8ad;
    --card-shadow: rgba(0, 0, 0, 0.35);
  }
  html, body {
    margin: 0;
    padding: 0;
    width: 1200px;
    height: 1000px;
    overflow: hidden;
    background: var(--page-bg);
    font-family: "PT Sans", "Myriad Pro", Arial, sans-serif;
  }
  .canvas {
    position: relative;
    width: 1200px;
    height: 1000px;
  }
  .card {
    position: absolute;
    left: 290px;
    width: 597px;
    height: 345px;
    box-shadow: 1px 2px 4px var(--card-shadow);
  }
  .card--front {
    top: 148px;
    background: var(--card-dark);
    display: flex;
    align-items: center;
    justify-content: center;
  }
  .card--back {
    top: 547px;
    background: var(--card-light);
  }
  .brand {
    display: flex;
    align-items: center;
    gap: 14px;
    font-weight: 700;
    white-space: nowrap;
  }
  .brand__dot {
    border-radius: 50%;
    flex: none;
  }
  .brand--front {
    font-size: 34px;
    color: var(--brand-sky);
  }
  .brand--front .brand__dot {
    width: 26px;
    height: 26px;
    background: var(--brand-sky);
  }
  .brand--back {
    position: absolute;
    top: 50px;
    left: 0;
    width: 100%;
    flex-direction: column;
    gap: 10px;
    font-size: 29px;
    color: var(--brand-navy);
  }
  .brand--back .brand__dot {
    width: 44px;
    height: 44px;
    background: var(--brand-sky);
  }
  .contact {
    position: absolute;
    top: 172px;
    left: 0;
    width: 592px;
    margin: 0;
    text-align: center;
    font-size: 17.5px;
    line-height: 22.5px;
    color: var(--text-main);
  }
  .contact p { margin: 0; }
  .online {
    position: absolute;
    right: 28px;
    top: 278px;
    margin: 0;
    text-align: right;
    font-size: 17.5px;
    line-height: 22.5px;
    color: var(--text-soft);
  }
  .online p { margin: 0; }
</style>
</head>
<body>
  <main class="canvas">
    <section class="card card--front" aria-label="Card front">
      <div class="brand brand--front">
        <span class="brand__dot"></span>
        <span class="brand__name">Tidemark Harbor</span>
      </div>
    </section>

    <section class="card card--back" aria-label="Card back">
      <div class="brand brand--back">
        <span class="brand__dot"></span>
        <span class="brand__name">Tidemark Harbor</span>
      </div>
      <div class="contact">
        <p class="contact__name">Your Name here</p>
        <p>mobile 0000 000 000</p>
        <p>office 00 0000 0000</p>
        <p>fax 00 0000 0000</p>
      </div>
      <div class="online">
        <p>your@email here.com.au</p>
        <p>www.your website.com.au</p>
      </div>
    </section>
  </main>
</body>
</html>
```